Packing for Razor Blade VELKORN

Dears: We need a packing design. The product is an Disposable Razor Blade. We are a company in Brazil.

The packing consists in a bag package which the Disposables Razos are placed. 5 units into each bag.

The bag is not 100% printed and should let a space to the customer see the razors inside. Some competitors uses oval circle. I attached competitor package (Dov Harborline)

The background color should be blue, this color tonality should vary its magnitude from dark blue to soft blue. Blue is a good color for personal care products because customer can take the impression of cleanness, especially for razor blade which has the fuction to shave.

You can feel free to add other colors however it can not be much colorfull because it may get trouble to printer company print it. Silver is good.

You can feel free to do details. You can feel free also to place the logo above the package or at bottom of it.

Dimmensions:
Heigh 24cm
Width 10cm

Featuring
- Featuring: Handle with Grip. In Portuguese - (Cabo Aderente)
- Featuring: 2 Razors. In portuguese - (Duas Lâminas)

Reason: I stayed many days with out providing feedbacks. I want to give more time for you .

Target Market(s)

Mans ( for woman we will design other package )

Requirements
Nice to have
• maybe some tears as a wet surface...
pls can feel free

```html
<!DOCTYPE html>
<html lang="en">
<head>
<meta charset="utf-8">
<title>VELKORN Disposable Razor Pack</title>
<link rel="stylesheet" href="https://fonts.googleapis.com/css2?family=Audiowide&display=swap">
<style>
  :root {
    --page-bg: #d4d6da;
    --navy-deep: #0d1a5c;
    --navy: #13288a;
    --blue-mid: #1f56c4;
    --blue-bright: #2f8fe0;
    --blue-soft: #5ab8ee;
    --window-light: #e9e8f6;
    --window-shade: #b9bedf;
    --text-white: #f4f7ff;
    --text-navy: #0a1446;
  }
  * { margin: 0; padding: 0; box-sizing: border-box; }
  html, body {
    width: 1200px;
    height: 1200px;
    overflow: hidden;
    background: var(--page-bg);
  }
  .canvas {
    position: relative;
    width: 1200px;
    height: 1200px;
  }
  .pack {
    position: absolute;
    left: 370px;
    top: 48px;
    width: 460px;
    height: 1104px;
    overflow: hidden;
    background: linear-gradient(160deg, var(--navy-deep) 0%, var(--navy) 30%, var(--blue-mid) 58%, var(--navy) 80%, var(--navy-deep) 100%);
  }
  .pack-waves {
    position: absolute;
    inset: 0;
    width: 100%;
    height: 100%;
  }
  .product-window {
    position: absolute;
    left: 48px;
    top: 22px;
    width: 350px;
    height: 545px;
    border-radius: 50%;
    background: radial-gradient(ellipse at 45% 40%, var(--window-light) 0%, var(--window-light) 45%, var(--window-shade) 100%);
  }
  .features {
    position: absolute;
    left: 0;
    width: 100%;
    top: 655px;
    text-align: center;
    font-family: "Audiowide", sans-serif;
    font-size: 40px;
    line-height: 1.22;
    letter-spacing: 2px;
    padding-right: 16px;
  }
  .features .feature-grip { color: var(--text-white); display: block; }
  .features .feature-blades { color: var(--text-navy); display: block; }
  .brand {
    position: absolute;
    left: 0;
    width: 100%;
    top: 985px;
    display: flex;
    justify-content: center;
    align-items: center;
    gap: 12px;
    padding-right: 16px;
  }
  .brand-dot {
    width: 16px;
    height: 16px;
    border-radius: 50%;
    background: var(--text-white);
  }
  .brand-name {
    font-family: "Audiowide", sans-serif;
    font-size: 30px;
    letter-spacing: 2px;
    color: var(--text-white);
  }
</style>
</head>
<body>
<main class="canvas">
  <section class="pack" aria-label="VELKORN disposable razor pack">
    <svg class="pack-waves" viewBox="0 0 460 1104" preserveAspectRatio="none" aria-hidden="true">
      <defs>
        <linearGradient id="wave-light" x1="0" y1="0" x2="1" y2="0">
          <stop offset="0" stop-color="#5ab8ee" stop-opacity="0"/>
          <stop offset="0.6" stop-color="#5ab8ee" stop-opacity="0.55"/>
          <stop offset="1" stop-color="#9ad6f7" stop-opacity="0.8"/>
        </linearGradient>
      </defs>
      <path d="M300 0 C 380 120 470 200 460 330 L460 0 Z" fill="url(#wave-light)" opacity="0.7"/>
      <path d="M0 560 C 120 520 260 660 460 600 L460 660 C 280 720 120 600 0 640 Z" fill="url(#wave-light)" opacity="0.45"/>
      <path d="M0 900 C 150 820 300 960 460 880 L460 930 C 300 1010 150 880 0 960 Z" fill="url(#wave-light)" opacity="0.35"/>
      <path d="M40 760 C 180 700 320 820 460 760" stroke="#8fd0f6" stroke-width="2" fill="none" opacity="0.5"/>
    </svg>

    <div class="product-window" role="img" aria-label="Clear window showing two blue disposable razors inside the pack"></div>

    <h1 class="features">
      <span class="feature-grip">handle<br>with grip</span>
      <span class="feature-blades">2 razors</span>
    </h1>

    <div class="brand">
      <span class="brand-dot"></span>
      <span class="brand-name">VELKORN</span>
    </div>
  </section>
</main>
</body>
</html>
```